Rollvane Supply .com

This website is simple!!!
Landing page background image should capture the customers attention!!! We will provide a image as a example of what we like. The purpose for this website is to provide customers with a clean easy way to request a quote for industrial casters and wheels by OEM’s as well as maintenance departments worldwide. Please see if you can follow our thought process below.
Customer comes to website, they are invited to Request a Quote by providing us with Manufacturer Name, Manufacturers Part # and quantity needed.
If this is not known the customer will complete will WP conversation format form answering about 10 questions
Or
Look up the part number in one of the 8 to 12 catalogs located in the Pagewhirl Deck format on our catalog page, or equal plug in .
When the client request a quote a account page will pop up request The following:
Clients first and last name
Email address
And optional questions
Company name and best contact number.
Once this is complete customer will hit SUBMIT.
The customers request will be in system. A email will be sent to Customer service notifying us the Quote Request has been made.
We will then build a quote for the customer with a good, better and best options. Customers Request a Quote submission may have more than one caster or wheel requested at a time, so website must allow this.
When the customer comes back into website there email address will come up as the account name and request a password be made for them. This will allow them to store quotes in their account for future needs. If quote is older than 30 day the system will trigger a button at the bottom of the quote for resubmit Request for updated quote.
Once customer reviews quote the quote can be Converted to order within the website.
Once Converted the system will send us a email and order will be processed.
We will need a Chat program that will text to CS the questions.
You will need to have high quality graphic design skills on your team.
We have found 2 plugins that would work nicely with our new website Pagewhirl decks to showcase our catalogs for customers to research and QuillKit conversation forms to complete request for quote form.
Just Ideas:
Very very ghosted caster blueprint in white background but very very ghosted or the icon just idea
We have never had a font used we like
Grayscale every except for rubber on wheels and logo icon
Website should have hamburger menu on left
Website should hav responsive deign
Account head on right side
Has anyone read the brief from top to bottom and the updates, I’m seeing a lot of duplicates of the website I posted in images I want a clean website With lite backgrand with the poly being definite colors on each wheel I added a green yellow and red image has anyone looked at that Just a question?
Went on vacation/holiday

```html
<!DOCTYPE html>
<html lang="en">
<head>
<meta charset="utf-8">
<title>Rollvane Supply — Website Pages</title>
<link href="https://fonts.googleapis.com/css2?family=Montserrat:wght@700;800&family=Fira+Sans:wght@400;500;600;700&display=swap" rel="stylesheet">
<style>
:root{
  --board:#b3b3b3;
  --brand:#2c4a9e;
  --brand-dark:#243f8c;
  --section:#40569e;
  --section-line:#7386c4;
  --frame:#b9c6f2;
  --accent-card:#5b76dc;
  --ink:#2b2b2b;
  --muted:#5d5d5d;
  --soft:#efefef;
  --field:#eef1f8;
  --white:#ffffff;
}
*{box-sizing:border-box;margin:0;padding:0}
html,body{width:1198px;height:1200px;overflow:hidden;background:var(--board)}
body{font-family:"Fira Sans",sans-serif;color:var(--ink)}
.stage{position:absolute;left:0;top:0;width:1929px;height:1932px;transform:scale(.6211);transform-origin:0 0}
.page{position:absolute;background:var(--white);overflow:hidden}
.abs{position:absolute}

/* hero */
.hero{position:absolute;left:0;top:0;width:578px;height:310px;
  background:linear-gradient(125deg,#f7f7f7 0%,#ececec 38%,#f4f4f4 39%,#e8e8e8 62%,#f1f1f1 63%,#e2e2e2 100%)}
.brand-mark{position:absolute;display:flex;align-items:center;gap:6px;color:var(--brand);font-weight:700;font-size:13px}
.brand-mark .dot{width:14px;height:14px;border-radius:50%;background:var(--brand)}
.burger{position:absolute;left:510px;top:16px;width:11px}
.burger i{display:block;height:2px;background:#222;margin-bottom:2.5px}
.hero-title{position:absolute;left:53px;top:96px;font-family:Montserrat,sans-serif;font-weight:800;font-size:22px;color:var(--brand);letter-spacing:.3px}
.hero-sub{position:absolute;left:53px;top:131px;font-size:11.5px;font-weight:500;color:#4a4a4a}
.hero-easy{position:absolute;left:53px;top:152px;font-size:8.5px;color:#444}
.hero-list{position:absolute;left:53px;top:170px;list-style:none}
.hero-list li{font-size:8.5px;color:#444;height:14.6px;display:flex;align-items:center;gap:8px}
.hero-list li svg{width:7px;height:7px}
.btn-dark{position:absolute;height:20px;background:var(--brand-dark);color:#fff;font-size:6.5px;font-weight:700;display:flex;align-items:center;justify-content:center;gap:5px;letter-spacing:.2px;box-shadow:0 2px 3px rgba(0,0,0,.2)}
.btn-dark b{width:6px;height:6px;border-radius:50%;background:#fff}
.caster-photo{position:absolute;left:296px;top:72px;width:230px;height:225px;border-radius:46% 46% 50% 50%;
  background:radial-gradient(ellipse at 40% 68%,#1e2e5c 0%,#2f437c 35%,#8d949e 62%,rgba(200,200,205,.5) 78%,rgba(235,235,235,0) 100%)}

/* headings */
.sec-title{position:absolute;left:0;width:578px;text-align:center;font-weight:600;font-size:15px}
.rule{position:absolute;height:1.5px;width:24px}
.sec-text{position:absolute;left:0;width:578px;text-align:center;font-size:9.5px;line-height:1.35}

/* catalog */
.cat-head{position:absolute;left:0;display:flex;align-items:center;justify-content:center;font-weight:700;font-size:16px;color:#fff}
.search{position:absolute;display:flex;align-items:center;padding-left:14px;font-size:10px}
.filters{position:absolute;left:0;padding-left:26px}
.filters h4{font-weight:400;font-size:9.5px;margin:14px 0 6px}
.filters label{display:flex;align-items:center;gap:7px;font-size:8.5px;height:20.5px}
.filters label i{width:6px;height:6px;border:1px solid currentColor;display:block}
.filters hr{border:0;border-top:1px solid var(--section-line);margin:8px 0 0 -26px}
.grid{position:absolute;display:grid;grid-template-columns:repeat(4,94px);column-gap:12px;row-gap:14px}
.card{height:109px;background:#fff;padding:4px;border:1px solid #d7d7d7}
.card .photo{width:100%;height:100%;border:1px solid #cfcfcf}
.grid.framed .card{border:3px solid var(--frame);padding:2px}
.grid.framed .card .photo{border:0}
.card.feature{background:var(--accent-card);color:#fff;text-align:center;padding:6px 8px}
.grid.framed .card.feature{border:3px solid var(--frame);outline:1px solid #3554c9;outline-offset:-4px}
.card.feature h5{font-size:8px;font-weight:600;margin:6px 0 4px}
.card.feature p{font-size:5.6px;line-height:1.5}
.card.feature span{display:block;margin-top:5px;font-size:6.5px;font-weight:700;text-decoration:underline}
.ph-caster{background:radial-gradient(circle at 50% 58%,#263a72 0%,#3d4d7c 22%,#b9bcc2 40%,#fff 62%)}
.ph-dark{background:radial-gradient(circle at 50% 50%,#9a9a9a 0%,#2c2c2c 16%,#1d1d1d 40%,#fff 48%)}
.ph-silver{background:radial-gradient(circle at 50% 50%,#5a5a5a 0%,#aaa 18%,#6d6d6d 38%,#fff 48%)}
.ph-blue{background:radial-gradient(circle at 50% 62%,#1e4aa0 0%,#2d2d2d 22%,#c8c8c8 38%,#fff 58%)}
.ph-rim{background:radial-gradient(circle at 50% 50%,#b6c4d4 0%,#3a3a3a 20%,#1a1a1a 40%,#fff 48%)}
.btn-pill{position:absolute;height:24px;border-radius:12px;display:flex;align-items:center;justify-content:center;font-size:9px;font-weight:500;box-shadow:0 2px 4px rgba(0,0,0,.25)}

/* steps */
.step-circle{position:absolute;width:72px;height:72px;border-radius:50%;background:#fff;box-shadow:0 1px 5px rgba(0,0,0,.25);display:flex;align-items:center;justify-content:center}
.step-title{position:absolute;width:170px;text-align:center;color:var(--brand);font-weight:700;font-size:11px}
.step-text{position:absolute;width:150px;text-align:center;color:var(--muted);font-size:8.5px;line-height:1.45}

/* footer */
.footer{position:absolute;left:0;width:578px;background:var(--soft)}
.wave{position:absolute;left:0;width:578px;height:60px}
.chat{position:absolute;width:52px;height:52px;border-radius:50%;background:var(--section);border:3px solid #c6cde6;box-shadow:0 3px 6px rgba(0,0,0,.3);display:flex;align-items:center;justify-content:center}
.f-col{position:absolute}
.f-col h6{color:var(--brand);font-size:10px;font-weight:600;letter-spacing:.2px}
.f-col .u{width:60px;height:1px;background:linear-gradient(90deg,var(--brand) 40%,#bbb 40%);margin:6px 0 10px}
.f-col a{display:block;font-size:7.5px;color:var(--brand);text-decoration:none;height:18.3px}
.f-col a:before{content:"» ";color:#333}
.f-contact p{font-size:7.5px;color:var(--brand);line-height:1.3;display:flex;gap:5px;padding-bottom:6px;margin-bottom:7px;border-bottom:1px solid #bbb;width:95px}
.f-brand{position:absolute;width:140px}
.f-brand .nm{display:flex;align-items:center;gap:6px;font-size:9px;font-weight:700;color:#111}
.f-brand .nm i{width:30px;height:30px;border-radius:50%;background:#111;display:block}
.f-brand p{font-size:7.3px;line-height:1.35;color:var(--brand);margin-top:10px;text-align:justify}
.socials{display:flex;gap:16px;margin-top:8px}
.socials i{width:14px;height:14px;border-radius:50%;border:1px solid var(--brand);display:block}
.f-line{position:absolute;left:53px;width:470px;height:1px;background:#bbb}
.copy{position:absolute;left:0;width:578px;text-align:center;font-size:6.5px;color:var(--brand)}

/* account */
.acc-bar{position:absolute;left:0;top:0;width:578px;height:38px;background:#fff;box-shadow:0 1px 2px rgba(0,0,0,.06)}
.nav-cat{position:absolute;top:15px;font-size:5px;color:#333}
.acc-search{position:absolute;left:337px;top:12px;width:91px;height:13px;border:1px solid #ddd;font-size:3.8px;color:#999;padding:4px 5px}
.acc-ico{position:absolute;top:11px;text-align:center;font-size:3.5px;color:#222}
.acc-ico i{display:block;width:7px;height:7px;margin:0 auto 2px;border:1px solid #222;border-radius:50%}
.side-item{position:absolute;left:58px;font-size:6.5px;display:flex;align-items:center;gap:6px;color:#222}
.side-item i{width:7px;height:7px;border:1px solid #333;border-radius:50%;display:block}
.acc-card{position:absolute;left:160px;top:62px;width:365px;height:591px;background:#fff;border:1px solid #dde0e8}
.acc-h{position:absolute;left:23px;font-size:7px;font-weight:700;color:#111}
.acc-p{position:absolute;left:23px;width:305px;font-size:4.8px;line-height:1.55;color:#444}
.acc-line{position:absolute;left:23px;width:318px;height:1px;background:#c9c9c9}
.field{position:absolute;width:149px;height:20px;background:var(--field);border:1px solid #e2e6f0;font-size:4.8px;color:var(--brand);font-weight:600;padding:7px 8px}
.save{position:absolute;left:23px;width:42px;height:18px;background:var(--brand-dark);color:#fff;font-size:6.5px;display:flex;align-items:center;justify-content:center}
</style>
</head>
<body>
<div class="stage">

<!-- ============ LANDING PAGE ============ -->
<section class="page" style="left:52px;top:57px;width:578px;height:1819px">
  <header class="hero">
    <div class="brand-mark" style="left:53px;top:14px"><span class="dot"></span>Rollvane</div>
    <div class="burger"><i></i><i></i><i></i></div>
    <h1 class="hero-title">ROLLVANE SUPPLY</h1>
    <p class="hero-sub"># 1 Solutions for all your Applications</p>
    <p class="hero-easy">Easy as 1 - 2 - 3</p>
    <ul class="hero-list">
      <li><svg viewBox="0 0 8 8"><circle cx="4" cy="4" r="3.5" fill="none" stroke="#2c4a9e"/><path d="M2.3 4.1l1.2 1.1 2.2-2.3" fill="none" stroke="#2c4a9e"/></svg>Request a Quote</li>
      <li><svg viewBox="0 0 8 8"><circle cx="4" cy="4" r="3.5" fill="none" stroke="#2c4a9e"/><path d="M2.3 4.1l1.2 1.1 2.2-2.3" fill="none" stroke="#2c4a9e"/></svg>Receive a Quote</li>
      <li><svg viewBox="0 0 8 8"><circle cx="4" cy="4" r="3.5" fill="none" stroke="#2c4a9e"/><path d="M2.3 4.1l1.2 1.1 2.2-2.3" fill="none" stroke="#2c4a9e"/></svg>Convert a Quote to order</li>
    </ul>
    <a class="btn-dark" style="left:53px;top:224px;width:88px">REQUEST A QUOTE <b></b></a>
    <a class="btn-dark" style="left:148px;top:224px;width:64px">CATALOG <b></b></a>
    <div class="caster-photo" role="img" aria-label="Swivel caster with navy rubber wheel"></div>
  </header>

  <div class="abs" role="img" aria-label="Photo of an empty warehouse interior" style="left:53px;top:358px;width:214px;height:212px;border:4px solid #d9d9d9;outline:2px solid #9e9e9e;background:linear-gradient(180deg,#6c6f73 0%,#a5a8ab 45%,#c9cacb 70%,#8e9092 100%)"></div>
  <h2 class="abs" style="left:296px;top:356px;font-size:14.5px;font-weight:500">About Rollvane Supply</h2>
  <div class="rule" style="left:296px;top:383px;background:var(--brand)"></div>
  <p class="abs" style="left:296px;top:396px;width:228px;font-size:8.6px;line-height:1.45;text-align:justify;color:#333">Ut enim ad minim veniam, quis nostrud exercitation ullamco laboris nisi ut aliquip ex ea commodo consequat. Duis aute irure dolor in reprehenderit in voluptate eiusmod tempor incididunt ut labore e velit esse cillum dolore eu fugiat nulla pariatur. Excepteur sint occaecat cupidatat non proident, sunt in culpa qui officia deserunt mollit anim id est laborum.</p>
  <p class="abs" style="left:296px;top:507px;width:228px;font-size:8.6px;line-height:1.45;color:#333">Ut enim ad minima veniam, quis nostrum exercitationem ullam corporis suscipit commodi consequatur.</p>
  <a class="btn-pill" style="left:296px;top:542px;width:74px;background:var(--brand-dark);color:#fff">Read More</a>

  <div class="abs" style="left:0;top:622px;width:578px;height:656px;background:var(--section);color:#fff">
    <h2 class="sec-title" style="top:48px">Our Product</h2>
    <div class="rule" style="left:277px;top:77px;background:#fff"></div>
    <p class="sec-text" style="top:89px">Duis aute irure dolor in reprehenderit in voluptate Quis autem vel eum iure<br>reprehenderit velit esse cillum dolore eu fugiat nulla pariatur.</p>
    <div class="abs" style="left:0;top:134px;width:578px;height:38px;border-top:1px solid var(--section-line);border-bottom:1px solid var(--section-line)"></div>
    <div class="cat-head" style="top:134px;width:113px;height:38px;border-right:1px solid var(--section-line)">Catalog</div>
    <div class="search" style="left:113px;top:134px;height:38px;color:#b9c3e6">Search Product......</div>
    <div class="filters" style="top:172px;width:113px;height:379px;border-right:1px solid var(--section-line);border-bottom:1px solid var(--section-line)">
      <h4>TYPE</h4>
      <label><i></i>All Types</label><label><i></i>Velit Esse</label><label><i></i>Dolore</label>
      <hr>
      <h4>MATERIALS</h4>
      <label><i></i>Consectetur</label><label><i></i>Undeomnis</label><label><i></i>Perspiciatis</label><label><i></i>Voluptas</label><label><i></i>Explicabo</label><label><i></i>Numquam</label>
      <hr>
      <h4>TYPE</h4>
      <label><i></i>All Types</label><label><i></i>Velit Esse</label><label><i></i>Dolore</label>
    </div>
    <div class="grid" style="left:128px;top:186px">
      <div class="card"><div class="photo ph-caster" role="img" aria-label="Swivel caster"></div></div>
      <div class="card feature"><h5>Finibus Bonorum</h5><p>Ut enim ad minim veniam, quis nostrud exercitation ullamco laboris nisi ut aliquip ex ea commodo.</p><span>SHOP NOW</span></div>
      <div class="card"><div class="photo ph-dark" role="img" aria-label="Dark spoked wheel"></div></div>
      <div class="card"><div class="photo ph-silver" role="img" aria-label="Grey pulley wheel"></div></div>
      <div class="card"><div class="photo ph-caster" role="img" aria-label="Rigid caster"></div></div>
      <div class="card"><div class="photo ph-dark" role="img" aria-label="Black solid wheel"></div></div>
      <div class="card"><div class="photo ph-silver" role="img" aria-label="Silver alloy wheel"></div></div>
      <div class="card"><div class="photo ph-dark" role="img" aria-label="Black rubber wheel"></div></div>
      <div class="card"><div class="photo ph-rim" role="img" aria-label="Wheel with chrome hub"></div></div>
      <div class="card"><div class="photo ph-blue" role="img" aria-label="Caster with blue wheel and brake"></div></div>
      <div class="card"><div class="photo ph-dark" role="img" aria-label="Black drilled pulley"></div></div>
      <div class="card"><div class="photo ph-silver" role="img" aria-label="Grooved grey pulley"></div></div>
    </div>
    <a class="btn-pill" style="left:257px;top:574px;width:64px;background:#fff;color:var(--brand)">View All</a>
  </div>

  <h2 class="sec-title" style="top:1318px">How Its Work</h2>
  <div class="rule" style="left:277px;top:1346px;background:#222"></div>
  <svg class="abs" style="left:0;top:1380px" width="578" height="60"><path d="M162 25 Q210 5 258 25" fill="none" stroke="#2c4a9e" stroke-dasharray="2 2"/><path d="M334 25 Q380 45 426 25" fill="none" stroke="#2c4a9e" stroke-dasharray="2 2"/></svg>
  <div class="step-circle" style="left:90px;top:1372px"><svg width="40" height="40" viewBox="0 0 40 40" fill="none" stroke="#2c4a9e" stroke-width="1.4"><rect x="5" y="9" width="26" height="19" rx="1"/><path d="M14 33h8M18 28v5"/><circle cx="27" cy="11" r="7" fill="#fff"/><path d="M27 9v6M27 7v.5"/></svg></div>
  <div class="step-circle" style="left:252px;top:1372px"><svg width="40" height="40" viewBox="0 0 40 40" fill="none" stroke="#2c4a9e" stroke-width="1.4"><rect x="10" y="5" width="20" height="28"/><path d="M14 11h12M14 15h12M14 19h12M14 24h5v5h-5zM22 25h4M22 28h4"/></svg></div>
  <div class="step-circle" style="left:424px;top:1372px"><svg width="40" height="40" viewBox="0 0 40 40" fill="none" stroke="#2c4a9e" stroke-width="1.4"><path d="M30 14a12 12 0 0 0-20-2M10 26a12 12 0 0 0 20 2M10 7v5h5M30 33v-5h-5"/><path d="M17 14l8 6-8 6z"/></svg></div>
  <h3 class="step-title" style="left:41px;top:1454px">Request A quote</h3>
  <p class="step-text" style="left:51px;top:1471px">Excepteur sint occaecat cupidatat non proident. sunt in culpa qui officia deserunt id est laborum.</p>
  <h3 class="step-title" style="left:203px;top:1454px">Recive A quote</h3>
  <p class="step-text" style="left:213px;top:1471px">Duis aute irure dolor in repreheerit in voluptate velit esse cillum dolore eu fugiat nulla pariatur.</p>
  <h3 class="step-title" style="left:375px;top:1454px">Convert a quote to order</h3>
  <p class="step-text" style="left:380px;top:1471px;width:160px">Quis autem vel eum iure reprehenderit qui in ea voluptate velit esse quam nihil molestiae</p>

  <div class="footer" style="top:1560px;height:259px"></div>
  <svg class="wave" style="top:1530px" viewBox="0 0 578 60"><path d="M0 14 Q280 70 578 10 L578 60 L0 60Z" fill="#efefef"/><path d="M0 14 Q280 70 578 10" fill="none" stroke="#2c4a9e" stroke-width="3"/></svg>
  <div class="chat" style="left:26px;top:1523px"><svg width="22" height="20" viewBox="0 0 22 20" fill="none" stroke="#fff" stroke-width="1.3"><path d="M2 2h13v9H7l-3 3v-3H2z"/><path d="M15 6h5v9h-2v3l-3-3H8v-4"/><path d="M5 5h7M5 8h5"/></svg></div>
  <div class="f-col" style="left:53px;top:1625px"><h6>QUICK LINKS</h6><div class="u"></div><a>Home</a><a>About</a><a>Product</a><a>Why choose us</a><a>Blog</a></div>
  <div class="f-col" style="left:154px;top:1625px"><h6>HELP CENTER</h6><div class="u"></div><a>FAQ</a><a>Privacy</a><a>Condition</a><a>Terms</a><a>Contact</a></div>
  <div class="f-col f-contact" style="left:253px;top:1625px"><h6>CONTACT US</h6><div class="u"></div><p><span>◎</span>Rollvane Supply<br>Fresno<br>California</p><p><span>✉</span>desk@rollvanesupply.com</p><p><span>✆</span>+1 555 014 2290</p></div>
  <div class="f-brand" style="left:388px;top:1628px"><div class="nm"><i></i>ROLLVANE SUPPLY.com</div><p>Excepteur sint occaecat cupidatat non proident, sunt in culpa qui officia deserunt mollit anim id est cillum dolore eu fugiat nulla pariatur laborum.</p><div class="socials"><i></i><i></i><i></i><i></i></div></div>
  <div class="f-line" style="top:1770px"></div>
  <p class="copy" style="top:1789px">Copyrights@2022.All Rights Reserved</p>
</section>

<!-- ============ CATALOG PAGE ============ -->
<section class="page" style="left:676px;top:57px;width:578px;height:1205px">
  <header class="hero">
    <div class="brand-mark" style="left:53px;top:14px"><span class="dot"></span>Rollvane</div>
    <div class="burger"><i></i><i></i><i></i></div>
    <h1 class="hero-title">ROLLVANE SUPPLY</h1>
    <p class="hero-sub"># 1 Solutions for all your Applications</p>
    <p class="hero-easy">Easy as 1 - 2 - 3</p>
    <ul class="hero-list">
      <li><svg viewBox="0 0 8 8"><circle cx="4" cy="4" r="3.5" fill="none" stroke="#2c4a9e"/><path d="M2.3 4.1l1.2 1.1 2.2-2.3" fill="none" stroke="#2c4a9e"/></svg>Request a Quote</li>
      <li><svg viewBox="0 0 8 8"><circle cx="4" cy="4" r="3.5" fill="none" stroke="#2c4a9e"/><path d="M2.3 4.1l1.2 1.1 2.2-2.3" fill="none" stroke="#2c4a9e"/></svg>Receive a Quote</li>
      <li><svg viewBox="0 0 8 8"><circle cx="4" cy="4" r="3.5" fill="none" stroke="#2c4a9e"/><path d="M2.3 4.1l1.2 1.1 2.2-2.3" fill="none" stroke="#2c4a9e"/></svg>Convert a Quote to order</li>
    </ul>
    <a class="btn-dark" style="left:53px;top:224px;width:88px">REQUEST A QUOTE <b></b></a>
    <a class="btn-dark" style="left:148px;top:224px;width:64px">CATALOG <b></b></a>
    <div class="caster-photo" role="img" aria-label="Swivel caster with navy rubber wheel"></div>
  </header>

  <h2 class="sec-title" style="top:348px;color:#222">Our Product</h2>
  <div class="rule" style="left:277px;top:375px;background:#222"></div>
  <p class="sec-text" style="top:389px;color:#555">Duis aute irure dolor in reprehenderit in voluptate Quis autem vel eum iure<br>reprehenderit velit esse cillum dolore eu fugiat nulla pariatur.</p>
  <div class="abs" style="left:0;top:434px;width:578px;height:38px;border-top:1.5px solid var(--section);border-bottom:1.5px solid var(--section)"></div>
  <div class="cat-head" style="top:434px;width:110px;height:38px;background:var(--section)">Catalog</div>
  <div class="search" style="left:110px;top:434px;height:38px;color:#888">Search Product......</div>
  <div class="filters" style="top:472px;width:110px;height:380px;background:var(--section);color:#fff">
    <h4>TYPE</h4>
    <label><i></i>All Types</label><label><i></i>Velit Esse</label><label><i></i>Dolore</label>
    <hr>
    <h4>MATERIALS</h4>
    <label><i></i>Consectetur</label><label><i></i>Undeomnis</label><label><i></i>Perspiciatis</label><label><i></i>Voluptas</label><label><i></i>Explicabo</label><label><i></i>Numquam</label>
    <hr>
    <h4>TYPE</h4>
    <label><i></i>All Types</label><label><i></i>Velit Esse</label><label><i></i>Dolore</label>
  </div>
  <div class="grid framed" style="left:127px;top:486px">
    <div class="card"><div class="photo ph-caster" role="img" aria-label="Swivel caster"></div></div>
    <div class="card feature"><h5>Finibus Bonorum</h5><p>Ut enim ad minim veniam, quis nostrud exercitation ullamco laboris nisi ut aliquip ex ea commodo.</p><span>SHOP NOW</span></div>
    <div class="card"><div class="photo ph-dark" role="img" aria-label="Dark spoked wheel"></div></div>
    <div class="card"><div class="photo ph-silver" role="img" aria-label="Grey pulley wheel"></div></div>
    <div class="card"><div class="photo ph-caster" role="img" aria-label="Rigid caster"></div></div>
    <div class="card"><div class="photo ph-dark" role="img" aria-label="Black solid wheel"></div></div>
    <div class="card"><div class="photo ph-silver" role="img" aria-label="Silver alloy wheel"></div></div>
    <div class="card"><div class="photo ph-dark" role="img" aria-label="Black rubber wheel"></div></div>
    <div class="card"><div class="photo ph-rim" role="img" aria-label="Wheel with chrome hub"></div></div>
    <div class="card"><div class="photo ph-blue" role="img" aria-label="Caster with blue wheel and brake"></div></div>
    <div class="card"><div class="photo ph-dark" role="img" aria-label="Black drilled pulley"></div></div>
    <div class="card"><div class="photo ph-silver" role="img" aria-label="Grooved grey pulley"></div></div>
  </div>
  <a class="btn-pill" style="left:256px;top:885px;width:64px;background:var(--brand-dark);color:#fff">View All</a>

  <div class="footer" style="top:955px;height:250px"></div>
  <svg class="wave" style="top:915px" viewBox="0 0 578 60"><path d="M0 16 Q290 68 578 10 L578 60 L0 60Z" fill="#efefef"/><path d="M0 16 Q290 68 578 10" fill="none" stroke="#2c4a9e" stroke-width="3"/></svg>
  <div class="chat" style="left:22px;top:910px"><svg width="22" height="20" viewBox="0 0 22 20" fill="none" stroke="#fff" stroke-width="1.3"><path d="M2 2h13v9H7l-3 3v-3H2z"/><path d="M15 6h5v9h-2v3l-3-3H8v-4"/><path d="M5 5h7M5 8h5"/></svg></div>
  <div class="f-col" style="left:53px;top:1011px"><h6>QUICK LINKS</h6><div class="u"></div><a>Home</a><a>About</a><a>Product</a><a>Why choose us</a><a>Blog</a></div>
  <div class="f-col" style="left:150px;top:1011px"><h6>HELP CENTER</h6><div class="u"></div><a>FAQ</a><a>Privacy</a><a>Condition</a><a>Terms</a><a>Contact</a></div>
  <div class="f-col f-contact" style="left:249px;top:1011px"><h6>CONTACT US</h6><div class="u"></div><p><span>◎</span>Rollvane Supply<br>Fresno<br>California</p><p><span>✉</span>desk@rollvanesupply.com</p><p><span>✆</span>+1 555 014 2290</p></div>
  <div class="f-brand" style="left:384px;top:1014px"><div class="nm"><i></i>ROLLVANE SUPPLY.com</div><p>Excepteur sint occaecat cupidatat non proident, sunt in culpa qui officia deserunt mollit anim id est cillum dolore eu fugiat nulla pariatur laborum.</p><div class="socials"><i></i><i></i><i></i><i></i></div></div>
  <div class="f-line" style="top:1155px;left:48px"></div>
  <p class="copy" style="top:1174px">Copyrights@2022.All Rights Reserved</p>
</section>

<!-- ============ ACCOUNT PAGE ============ -->
<section class="page" style="left:1303px;top:57px;width:578px;height:690px;background:#eef0f4">
  <header class="acc-bar">
    <div class="brand-mark" style="left:55px;top:12px;font-size:9.5px;gap:5px"><span class="dot" style="width:10px;height:10px"></span>ROLLVANE SUPPLY</div>
    <span class="nav-cat" style="left:188px">CATEGORY 1</span>
    <span class="nav-cat" style="left:237px">CATEGORY 1</span>
    <span class="nav-cat" style="left:287px">CATEGORY 1</span>
    <div class="acc-search">Search</div>
    <div class="acc-ico" style="left:446px;width:24px"><i></i>MY ACCOUNT</div>
    <div class="acc-ico" style="left:480px;width:20px"><i></i>WISHLIST</div>
    <div class="acc-ico" style="left:508px;width:20px"><i></i>₹0.00</div>
  </header>
  <p class="abs" style="left:48px;top:50px;font-size:6.5px">Homepage / <span style="color:var(--brand)">My Account</span></p>
  <h2 class="abs" style="left:48px;top:73px;font-size:13px;font-weight:500">My Account</h2>
  <div class="abs" style="left:48px;top:103px;width:92px;height:22px;background:#d9e1f8"></div>
  <div class="side-item" style="top:110px;color:var(--brand)"><i style="border-color:var(--brand)"></i>My Details</div>
  <div class="side-item" style="top:137px"><i></i>Shipping Address</div>
  <div class="side-item" style="top:158px"><i></i>My Orders</div>
  <div class="side-item" style="top:179px"><i></i>Help</div>
  <div class="side-item" style="top:200px"><i></i>Privacy</div>
  <div class="side-item" style="top:221px"><i></i>Account Settings</div>

  <div class="acc-card">
    <h3 class="abs" style="left:23px;top:20px;font-size:11.5px;font-weight:500">My Details</h3>
    <p class="acc-h" style="top:47px">Personel Information</p>
    <p class="acc-p" style="top:60px">Lorem ipsum dolor sit amet, consectetur adipiscing elit, sed do eiusmod tempor incididunt ut labore et dolore magna aliqua. Ut enim ad minim veniam, quis nostrud exercitation ullamco lo consequat.</p>
    <div class="acc-line" style="top:86px"></div>
    <div class="field" style="left:23px;top:97px">First Name*</div>
    <div class="field" style="left:192px;top:97px">Last Name*</div>
    <div class="field" style="left:23px;top:128px">Birth Date*</div>
    <div class="field" style="left:192px;top:128px">Phone Number*</div>
    <div class="save" style="top:161px">Save</div>
    <p class="acc-h" style="top:205px">Email Address</p>
    <p class="acc-p" style="top:220px">Duis aute irure dolor in reprehenderit in voluptate velit esse cillum dolore eu fugiat nulla pariatur. Excepteur sint occaecat cupidatat non proident, sunt in culpa qui officia deserunt mollit anim id est laborum.</p>
    <div class="acc-line" style="top:244px"></div>
    <div class="field" style="left:23px;top:255px">Email Address*</div>
    <div class="save" style="top:289px">Save</div>
    <p class="acc-h" style="top:336px">Address</p>
    <p class="acc-p" style="top:351px">Nemo enim ipsam voluptatem quia voluptas sit aspernatur aut odit aut fugit, sed quia consequuntur magni dolores eos qui ratione voluptatem sequi nesciunt.</p>
    <div class="acc-line" style="top:375px"></div>
    <div class="field" style="left:23px;top:386px">Address*</div>
    <div class="field" style="left:192px;top:386px">Country*</div>
    <div class="field" style="left:23px;top:417px">Pincode*</div>
    <div class="save" style="top:454px">Save</div>
    <div class="acc-line" style="top:499px"></div>
    <p class="acc-p" style="top:515px;left:40px;width:285px;text-align:center">Quis autem vel eum iure reprehenderit qui in ea voluptate velit esse quam nihil molestiae consequatur, vel illum qui dolorem eum fugiat quo voluptas nulla pariatur</p>
    <div class="save" style="left:129px;top:547px;width:98px">Submit Information</div>
  </div>
</section>

</div>
</body>
</html>
```